Ridgeline Outfitters Business Cards

Recently had a logo done with Artfolio and now looking for a business card to go along with it.

Target Market(s)

Ridgeline Outfitters is a weapons dealer. My market will be primarily men, hunting, shooting type.

Industry/Entity Type

Business

Contact Information for Business Card

I selected double sided, but this is not required, single or double is going to be fine. I picture the logo on one side, or perhaps just the circle which contains "RO" with the remaining info on the other side.

Font styles to use
Sans Serif

Requirements
Must have
• My name: Milo Brandt
• Title: Owner
• tel: 612-555-0187
• web: www.ridgelineoutfittersmn.example
Nice to have
• I like the concept of a black business card. I would like to keep the colors monotone, black, grey, white or red. Red is acceptable because it is in the logo. I have also seen cards that are matte black with shiny black as well, perhaps for the logo (or circle RO) part of the logo.
• I will upload a couple of the logos for use, and also an example I just found of the black on black. and some others that have a nice contrast.
Should not have
• lots of colors are not wanted.

```html
<!DOCTYPE html>
<html lang="en">
<head>
<meta charset="utf-8">
<title>Ridgeline Outfitters Business Cards</title>
<link rel="stylesheet" href="https://fonts.googleapis.com/css2?family=Open+Sans:wght@400;600&display=swap">
<style>
  :root {
    --backdrop: #3b3330;
    --card-grey: #7b7b7b;
    --card-black: #0c0c0c;
    --ink: #141414;
    --ink-soft: #2a2a2a;
    --gloss: #3e3e3e;
  }
  * { margin: 0; padding: 0; box-sizing: border-box; }
  html, body { width: 1200px; height: 844px; overflow: hidden; }
  body {
    background: var(--backdrop);
    font-family: "Open Sans", Arial, sans-serif;
    position: relative;
  }
  .card {
    position: absolute;
    width: 520px;
    height: 298px;
    border-radius: 2px;
  }
  .card-front {
    left: 50px;
    top: 273px;
    background: var(--card-grey);
    color: var(--ink);
  }
  .card-back {
    left: 630px;
    top: 273px;
    background: var(--card-black);
    color: var(--gloss);
  }
  .brand {
    position: absolute;
    display: flex;
    align-items: center;
    gap: 14px;
  }
  .card-front .brand { left: 150px; top: 44px; }
  .card-back .brand { left: 50%; top: 50%; transform: translate(-50%, -50%); }
  .brand-circle {
    width: 58px;
    height: 58px;
    border-radius: 50%;
    border: 5px solid currentColor;
    flex: none;
  }
  .brand-name {
    font-weight: 600;
    font-size: 22px;
    letter-spacing: 1px;
    text-transform: uppercase;
    white-space: nowrap;
  }
  .contact {
    position: absolute;
    left: 34px;
    bottom: 28px;
  }
  .contact-name {
    font-size: 21px;
    font-weight: 400;
    letter-spacing: 1px;
    text-transform: uppercase;
  }
  .contact-title {
    font-size: 13px;
    color: var(--ink-soft);
    margin: 2px 0 12px;
  }
  .contact-line {
    display: flex;
    align-items: center;
    gap: 8px;
    font-size: 14px;
    color: var(--ink-soft);
    margin-top: 4px;
  }
  .contact-line svg { width: 12px; height: 12px; fill: var(--ink); flex: none; }
</style>
</head>
<body>
  <section class="card card-front">
    <div class="brand">
      <span class="brand-circle"></span>
      <span class="brand-name">Ridgeline Outfitters</span>
    </div>
    <div class="contact">
      <p class="contact-name">Milo Brandt</p>
      <p class="contact-title">Owner</p>
      <p class="contact-line">
        <svg viewBox="0 0 24 24" aria-hidden="true"><path d="M6.6 10.8a15.1 15.1 0 0 0 6.6 6.6l2.2-2.2a1 1 0 0 1 1-.25 11.4 11.4 0 0 0 3.6.57 1 1 0 0 1 1 1V20a1 1 0 0 1-1 1A17 17 0 0 1 3 4a1 1 0 0 1 1-1h3.5a1 1 0 0 1 1 1c0 1.25.2 2.45.57 3.6a1 1 0 0 1-.25 1z"/></svg>
        612-555-0187
      </p>
      <p class="contact-line">
        <svg viewBox="0 0 24 24" aria-hidden="true"><circle cx="12" cy="12" r="11"/></svg>
        www.ridgelineoutfittersmn.example
      </p>
    </div>
  </section>
  <section class="card card-back">
    <div class="brand">
      <span class="brand-circle"></span>
      <span class="brand-name">Ridgeline Outfitters</span>
    </div>
  </section>
</body>
</html>
```